Business Card and Stationery for Interior Design Firm
Renata's Interiors
Business Card and Stationery for Interior Design Firm - Home and Garden
Creative Brief
Traditional
Renata Balsam
4837 Pinecrest Dr., Ste. 204 Carrollton, TX 75006
renata@renatas-interiors.example
www.renatas-interiors.example
I've included the address, but it does not have to be on the card. It is more important that the card is eye-catching and not too crowded. Love raised print, considering a background design of a perhaps a greek key, which is what I've used on my website. Think classic but on trend, and it needs to look expensive and be done on excellent paper. Right now I have a black and white raised background design (that is very dated) and on top of that on a white background framed in black is my info, so it sets it apart from the design. We don't need to re-create, but the overall card should really catch the eye. I also like cards with cut-outs. Colors should have continuity with my logo - grays, blacks and whites. The cards are coming back too brown so it is okay to tweak the logo so that is is more gray. It would help to look at my website to get a better feel for my style as well.
Much more simple. If a frame is used on the front, repeat on the back. Info to include is: Renata Balsam Allied GLHU PVR Professional TWRG www.social.example/RenatasInteriors

```html
<!DOCTYPE html>
<html lang="en">
<head>
<meta charset="utf-8">
<title>Renata's Interiors – Business Card</title>
<link rel="stylesheet" href="https://fonts.googleapis.com/css2?family=Tinos:wght@400;700&display=swap">
<style>
  :root {
    --backdrop: #e6e4e2;
    --paper: #ffffff;
    --paper-edge: #d8d5d2;
    --ink: #3a3634;
    --ink-soft: #6a6461;
    --taupe: #6e655f;
    --border-band: #c9c5c1;
    --border-band-dark: #9e9893;
  }
  * { box-sizing: border-box; margin: 0; padding: 0; }
  html, body { width: 1200px; height: 785px; overflow: hidden; }
  body {
    position: relative;
    background: var(--backdrop);
    font-family: "Tinos", "Times New Roman", serif;
    color: var(--ink);
  }
  .card {
    position: absolute;
    width: 520px;
    height: 297px;
    background: var(--paper);
    border: 1px solid var(--paper-edge);
    box-shadow: 0 2px 6px rgba(0,0,0,0.12);
  }
  .card--front { left: 60px; top: 60px; }
  .card--back { left: 620px; top: 428px; }

  .key-band {
    position: absolute;
    left: 14px;
    right: 14px;
    height: 16px;
    background: linear-gradient(90deg, var(--border-band), var(--border-band-dark) 50%, var(--border-band));
  }
  .key-band--top { top: 12px; }
  .key-band--bottom { bottom: 12px; }

  .brand {
    position: absolute;
    display: flex;
    flex-direction: column;
    align-items: center;
  }
  .brand__square { background: var(--taupe); }
  .brand__name {
    margin-top: 6px;
    font-size: 11px;
    letter-spacing: 0.5px;
    text-transform: uppercase;
    color: var(--taupe);
    white-space: nowrap;
  }

  .card--front .brand { left: 40px; top: 48px; }
  .card--front .brand__square { width: 96px; height: 96px; }

  .contact {
    position: absolute;
    left: 40px;
    top: 196px;
    font-size: 12px;
    color: var(--ink-soft);
  }
  .contact__line { display: flex; align-items: center; gap: 6px; }
  .contact__divider { margin: 0 8px; color: var(--ink-soft); }
  .contact__web { margin-top: 10px; font-weight: 700; color: var(--ink); }
  .contact svg { width: 12px; height: 12px; }

  .card--back .brand { left: 70px; top: 88px; }
  .card--back .brand__square { width: 84px; height: 84px; }
  .card--back .brand__name { font-size: 10px; }

  .person {
    position: absolute;
    left: 232px;
    top: 86px;
    line-height: 1.18;
  }
  .person__name { font-size: 22px; font-weight: 700; color: var(--ink); }
  .person__credential { font-size: 17px; color: var(--ink); }

  .social {
    position: absolute;
    left: 140px;
    top: 232px;
    display: flex;
    align-items: center;
    gap: 8px;
    font-size: 13px;
    color: var(--ink-soft);
  }
  .social__square { width: 13px; height: 13px; background: var(--ink-soft); }

  .logo-block {
    position: absolute;
    left: 200px;
    top: 470px;
    width: 250px;
    display: flex;
    flex-direction: column;
    align-items: center;
  }
  .logo-block__frame {
    width: 170px;
    height: 170px;
    border: 6px solid var(--paper);
    background: var(--taupe);
  }
  .logo-block__name {
    margin-top: 14px;
    font-size: 18px;
    letter-spacing: 1px;
    text-transform: uppercase;
    color: var(--ink);
  }
</style>
</head>
<body>

  <section class="card card--front" aria-label="Business card front">
    <div class="key-band key-band--top" role="img" aria-label="Greek key border pattern"></div>

    <div class="brand">
      <div class="brand__square"></div>
      <div class="brand__name">Renata's Interiors</div>
    </div>

    <div class="contact">
      <div class="contact__line">
        <svg viewBox="0 0 12 12" aria-hidden="true"><rect x="0.5" y="0.5" width="11" height="11" fill="none" stroke="currentColor"/><path d="M3 3.5 h2 l0.6 1.6 -1 0.7 a4 4 0 0 0 1.6 1.6 l0.7 -1 1.6 0.6 v2 a1 1 0 0 1 -1 1 a6 6 0 0 1 -5.5 -5.5 a1 1 0 0 1 1 -1z" fill="currentColor"/></svg>
        <span>555.010.2048</span>
        <span class="contact__divider">|</span>
        <svg viewBox="0 0 12 12" aria-hidden="true"><rect x="0.5" y="2.5" width="11" height="7" fill="none" stroke="currentColor"/><path d="M0.5 2.5 L6 7 L11.5 2.5" fill="none" stroke="currentColor"/></svg>
        <span>renata@renatas-interiors.example</span>
      </div>
      <div class="contact__web">www.renatas-interiors.example</div>
    </div>

    <div class="key-band key-band--bottom" role="img" aria-label="Greek key border pattern"></div>
  </section>

  <div class="logo-block">
    <div class="logo-block__frame"></div>
    <div class="logo-block__name">Renata's Interiors</div>
  </div>

  <section class="card card--back" aria-label="Business card back">
    <div class="key-band key-band--top" role="img" aria-label="Greek key border pattern"></div>

    <div class="brand">
      <div class="brand__square"></div>
      <div class="brand__name">Renata's Interiors</div>
    </div>

    <div class="person">
      <div class="person__name">Renata Balsam</div>
      <div class="person__credential">Allied GLHU</div>
      <div class="person__credential">PVR Professional</div>
      <div class="person__credential">TWRG</div>
    </div>

    <div class="social">
      <div class="social__square"></div>
      <span>www.social.example/RenatasInteriors</span>
    </div>

    <div class="key-band key-band--bottom" role="img" aria-label="Greek key border pattern"></div>
  </section>

</body>
</html>
```